ReDesign Website for a more Bold approach

Hello! I'd like to redesign my website: holvencrest.com

I'd like to add one thing that's not on my website which is a blog. The design around the blog should be put time into as I will be putting out incredibly great content and want it to attract viewers.

I get a lot of inspiration from ruvtal.com (the way they flow the big statements across each screen, colors)
moorlane.vc (the simplicity behind the design is beautiful)

I like modern very simple but bold approaches.

I am going to attach my logo here and if it can be thought of when making the design of the website. Thanks!

Industry/Entity Type

Finance and Private Equity

Number of Pages Required

3 page

Font styles to use
Serif
Sans Serif

Colors
0054AA
0677BA
7BADD7
CADEEF
E8F1F8
0094D4
00A9DD
6FCCEA
C7EBF8
E9F6FB
00AB8E
00BBA5
67D7C9
C6EFE9
E9F9F6

Requirements
Must have
• My project must have a Home, Expertise, Story, Clients, Approach, Blog, Contact
Nice to have
• It would be nice to have these tabs reduced to 1-3 pages
Should not have
• My project must not have bright colors.

```html
<!DOCTYPE html>
<html lang="en">
<head>
<meta charset="utf-8">
<title>Holvencrest Ventures</title>
<link rel="stylesheet" href="https://fonts.googleapis.com/css2?family=Montserrat:wght@400;500;600;700&family=Roboto:wght@400;500&display=swap">
<style>
:root{
  --navy:#0b3f98;
  --ink:#111418;
  --body:#3c4047;
  --white:#ffffff;
  --teal-bg:#aadfe0;
  --teal-deep:#86d0d4;
  --sky:#1b97d3;
  --sky-deep:#0c7fc0;
  --footer:#1c1c1e;
  --line:#d9dde2;
}
*{box-sizing:border-box;margin:0;padding:0}
html,body{width:1200px;height:4079px;overflow:hidden}
body{font-family:"Roboto",Arial,sans-serif;color:var(--body);background:var(--white);position:relative}
section,header,footer{position:absolute;left:0;width:1200px;overflow:hidden}
.abs{position:absolute}
h1,h2,h3,.brand{font-family:"Montserrat",Arial,sans-serif;font-weight:700;text-transform:uppercase}
.section-title{font-size:40px;color:var(--ink);text-align:center;letter-spacing:.3px}

/* hero */
.hero{top:0;height:641px;background:linear-gradient(160deg,#1f2f4c 0%,#2a4a78 35%,#3a5f8c 55%,#8a7550 78%,#2a3550 100%)}
.brand{color:var(--white);font-size:28px;top:26px;left:111px;letter-spacing:.3px}
.nav{top:34px;right:111px;display:flex;gap:34px;list-style:none;font-family:"Montserrat",sans-serif;font-size:14.5px}
.nav a{color:var(--white);text-decoration:none}
.nav .active{text-decoration:underline;text-underline-offset:5px}
.hero h1{top:254px;left:111px;color:var(--white);font-size:35px;line-height:45px}
.btn-ghost{top:367px;left:111px;width:202px;height:48px;border:1.5px solid var(--white);color:var(--white);font-family:"Montserrat",sans-serif;font-size:14px;display:flex;align-items:center;justify-content:center;text-transform:uppercase}
.scroll-arrow{top:518px;left:116px}

/* story */
.story{top:641px;height:617px}
.story-photo{left:0;top:0;width:600px;height:617px;background:linear-gradient(135deg,#a8aeb6,#e6e8ea 50%,#c9b89a)}
.story h2{left:649px;top:78px;font-size:40px;color:var(--ink)}
.story-text{left:649px;top:139px;width:440px;font-size:13px;line-height:28.5px;text-align:justify}
.story-text p+p{margin-top:15px}
.btn-solid{left:649px;top:486px;width:159px;height:46px;background:var(--navy);color:var(--white);font-family:"Montserrat",sans-serif;font-size:14px;display:flex;align-items:center;justify-content:center;text-transform:uppercase}

/* expertise */
.expertise{top:1258px;height:742px;background:linear-gradient(135deg,#b6e4e4 0%,var(--teal-bg) 50%,var(--teal-deep) 100%)}
.expertise .section-title{top:78px;width:100%}
.grid-line{background:rgba(255,255,255,.35)}
.skill{width:355px;text-align:center}
.skill .icon{width:66px;height:72px;margin:0 auto;background:rgba(11,63,152,.18);border-radius:8px}
.skill h3{margin-top:22px;font-size:17px;color:var(--ink);letter-spacing:.2px}
.skill p{margin-top:12px;font-size:13.5px;line-height:28.5px;color:#1e2a30}

/* approach */
.approach{top:2000px;height:533px;background:linear-gradient(120deg,#1d94d0 0%,var(--sky) 45%,#4fb3de 70%,var(--sky-deep) 100%)}
.approach h2{left:128px;top:77px;font-size:40px;color:var(--white)}
.approach p{color:var(--white);font-size:13px;line-height:28.5px;text-align:justify}
.approach .intro{left:128px;top:141px;width:440px}
.approach .col-left{left:128px;top:209px;width:440px}
.approach .col-right{left:625px;top:209px;width:432px;text-align:left}

/* blog */
.blog{top:2533px;height:646px}
.blog .section-title{top:87px;width:100%}
.card{top:161px;width:311px;height:394px;border:1px solid var(--line);background:var(--white)}
.card .photo{height:211px;background:linear-gradient(135deg,#5a5048,#b7a48c 55%,#3d3a38)}
.card .body{padding:20px 14px 0 14px}
.card .date{font-size:10.5px;color:#333;display:flex;align-items:center;gap:6px}
.card h3{margin-top:14px;font-size:16px;text-transform:none;font-weight:600;color:var(--ink)}
.card .excerpt{margin-top:10px;font-size:11.5px;line-height:23px;color:#444}
.card .meta{position:absolute;left:14px;right:14px;bottom:18px;display:flex;align-items:center;font-size:13px;color:#333}
.card .meta span{display:flex;align-items:center;gap:6px;margin-right:20px}
.card .meta .likes{margin-left:auto;margin-right:0}

/* contact */
.contact{top:3179px;height:573px;background:linear-gradient(120deg,#138cc9 0%,var(--sky) 50%,#2aa5dc 100%)}
.contact .section-title{top:102px;width:100%;color:var(--white)}
.field{background:var(--white);border:1px solid #cfd6dc;font-size:14px;color:#333;padding:0 13px;display:flex;align-items:center}
.field.area{align-items:flex-start;padding-top:18px}
.btn-submit{left:503px;top:437px;width:194px;height:52px;border:2px solid var(--white);color:var(--white);font-family:"Montserrat",sans-serif;font-size:15px;display:flex;align-items:center;justify-content:center;text-transform:uppercase}

/* footer */
.site-footer{top:3752px;height:327px;background:var(--footer);color:var(--white)}
.site-footer .brand{font-size:23px;top:66px;left:111px}
.foot-about{left:111px;top:108px;width:290px;font-size:11.5px;line-height:28.5px}
.site-footer h4{font-family:"Montserrat",sans-serif;font-weight:500;font-size:16px;text-transform:uppercase}
.foot-col{top:58px}
.contact-item{display:flex;gap:20px;margin-top:18px;font-size:13px;line-height:24px}
.contact-item .lbl{text-transform:uppercase;font-size:14px}
.links{list-style:none;margin-top:12px;font-size:12px;line-height:26px}
.social{display:flex;align-items:center;gap:14px;margin-top:14px;font-size:13.5px}
.social .dot{width:38px;height:38px;border:1px solid #888;border-radius:50%}
.foot-rule{left:111px;top:261px;width:978px;height:1px;background:#555}
.copyright{top:283px;width:100%;text-align:center;font-size:12px}
</style>
</head>
<body>

<header class="hero">
  <div class="abs" style="inset:0" role="img" aria-label="Photo looking up at glass skyscrapers against a cloudy sky with warm sunlight"></div>
  <div class="abs brand">Holvencrest Ventures</div>
  <ul class="abs nav">
    <li><a class="active" href="#">Home</a></li>
    <li><a href="#">Expertise</a></li>
    <li><a href="#">Story</a></li>
    <li><a href="#">Clients</a></li>
    <li><a href="#">Approach</a></li>
    <li><a href="#">Blog</a></li>
    <li><a href="#">Contact</a></li>
  </ul>
  <h1 class="abs">Built by founders<br>for founders</h1>
  <a class="abs btn-ghost">Get Started</a>
  <svg class="abs scroll-arrow" width="26" height="40" viewBox="0 0 26 40" fill="none" stroke="#fff" stroke-width="1.6"><path d="M13 1v37M2 27l11 11 11-11"/></svg>
</header>

<section class="story">
  <div class="abs story-photo" role="img" aria-label="Photo of a team reviewing charts and sticky notes on a table"></div>
  <h2 class="abs">Our Story</h2>
  <div class="abs story-text">
    <p>Holvencrest Ventures is a venture capital studio firm based in Austin TX with a laser focus on raising solid capital for startups and helping businesses jumpstart their revenue.</p>
    <p>Founded in 2020 by investment expert Marcus Holden, Holvencrest Ventures combines proven experience in the venture capital field with a data-driven business analysis strategy to secure capital and reinforce revenue streams for startups and established businesses. Born from the idea that the best way to help founders thrive is to understand their strengths, their weaknesses, their ambitions and their needs - our specialists have been through the entire startup process themselves, and that experience forms our unique approach to business support.</p>
  </div>
  <a class="abs btn-solid">Learn More</a>
</section>

<section class="expertise">
  <h2 class="abs section-title">Area of Expertise</h2>
  <div class="abs grid-line" style="left:416px;top:180px;width:1px;height:500px"></div>
  <div class="abs grid-line" style="left:777px;top:180px;width:1px;height:500px"></div>
  <div class="abs grid-line" style="left:70px;top:423px;width:1060px;height:1px"></div>

  <div class="abs skill" style="left:67px;top:182px"><div class="icon" role="img" aria-label="Network icon"></div><h3>Network Support</h3><p>Help you build your network, introducing<br>you to the right people in the right places.</p></div>
  <div class="abs skill" style="left:422px;top:182px"><div class="icon" role="img" aria-label="Marketing megaphone icon"></div><h3>Marketing</h3><p>Consult on marketing process, strategies<br>and implementation across your startup.</p></div>
  <div class="abs skill" style="left:777px;top:182px"><div class="icon" role="img" aria-label="Growing capital chart icon"></div><h3>Raising Capital</h3><p>Reach out to our extensive connections to<br>raise vital capital for your startup.</p></div>

  <div class="abs skill" style="left:67px;top:467px"><div class="icon" role="img" aria-label="Merging puzzle pieces icon"></div><h3>Mergers &amp; Acquistions</h3><p>Facilitate a smooth mergers and acquisition<br>process for the expansion of your business.</p></div>
  <div class="abs skill" style="left:422px;top:467px"><div class="icon" role="img" aria-label="Rocket icon"></div><h3>Revenue Acceleration</h3><p>Analyze your revenue streams, providing<br>solutions for kickstarting your revenue.</p></div>
  <div class="abs skill" style="left:777px;top:467px"><div class="icon" role="img" aria-label="Handshake icon"></div><h3>Integration &amp; Incubation</h3><p>Providing training and guidance for startups<br>looking to make their mark on the world.</p></div>
</section>

<section class="approach">
  <div class="abs" style="left:600px;top:0;width:600px;height:533px;background:linear-gradient(120deg,rgba(255,255,255,0),rgba(255,255,255,.12))" role="img" aria-label="Faded photo of a hand writing over financial charts"></div>
  <h2 class="abs">Our Approach</h2>
  <p class="abs intro">We've built our approach to helping your startup thrive based around three key developmental pillars that guarantee results for our partners.</p>
  <p class="abs col-left">First pillar is expertise. We've built our firm on a bank of insights, knowledge and proficiencies honed over years of working with the biggest names in venture capitalism – that experience forms the backbone of every project, every pitch and every investment. Second pillar is collaboration. We believe that the best partnerships start with a combined and cooperative approach that benefits all parties every step of the way. We'll always keep our partners up-to-date with our work using regular touchpoints and reports.</p>
  <p class="abs col-right">Third and final pillar is trust. We know that our clients and our partners know their industry better than we do, so we trust their input and their ideas – pairing them up with our own business intelligence to guarantee success.</p>
</section>

<section class="blog">
  <h2 class="abs section-title">Latest Blog</h2>
  <article class="abs card" style="left:111px">
    <div class="photo" role="img" aria-label="Photo of colleagues working around a desk with papers and coffee"></div>
    <div class="body">
      <div class="date"><svg width="11" height="11" viewBox="0 0 11 11"><rect x="0.5" y="1.5" width="10" height="9" fill="none" stroke="#333"/><rect x="0.5" y="1.5" width="10" height="2.5" fill="#333"/></svg>Dec 23, 2021</div>
      <h3>The standard Lorem Ipsum</h3>
      <p class="excerpt">Lorem ipsum dolor sit amet, consectetur adipiscing elit, sed do eiusmod tempor incididunt</p>
    </div>
    <div class="meta"><span><svg width="16" height="10" viewBox="0 0 16 10"><ellipse cx="8" cy="5" rx="7.5" ry="4.5" fill="#333"/><circle cx="8" cy="5" r="2" fill="#fff"/></svg>0</span><span><svg width="15" height="12" viewBox="0 0 15 12"><ellipse cx="7.5" cy="5" rx="6.5" ry="4.3" fill="none" stroke="#333" stroke-width="1.2"/><path d="M3 8.5L1.5 11.5 5.5 9.3" fill="none" stroke="#333" stroke-width="1.2"/></svg>0</span><span class="likes">2 <svg width="15" height="13" viewBox="0 0 15 13"><path d="M7.5 12L1.6 6.2A3.3 3.3 0 017.5 2.3a3.3 3.3 0 015.9 3.9z" fill="none" stroke="#333" stroke-width="1.2"/></svg></span></div>
  </article>
  <article class="abs card" style="left:445px">
    <div class="photo" style="background:linear-gradient(135deg,#3e4650,#c9ccd0 55%,#6b7178)" role="img" aria-label="Photo of business people reviewing printed charts"></div>
    <div class="body">
      <div class="date"><svg width="11" height="11" viewBox="0 0 11 11"><rect x="0.5" y="1.5" width="10" height="9" fill="none" stroke="#333"/><rect x="0.5" y="1.5" width="10" height="2.5" fill="#333"/></svg>Dec 23, 2021</div>
      <h3>The standard Lorem Ipsum</h3>
      <p class="excerpt">Lorem ipsum dolor sit amet, consectetur adipiscing elit, sed do eiusmod tempor incididunt</p>
    </div>
    <div class="meta"><span><svg width="16" height="10" viewBox="0 0 16 10"><ellipse cx="8" cy="5" rx="7.5" ry="4.5" fill="#333"/><circle cx="8" cy="5" r="2" fill="#fff"/></svg>0</span><span><svg width="15" height="12" viewBox="0 0 15 12"><ellipse cx="7.5" cy="5" rx="6.5" ry="4.3" fill="none" stroke="#333" stroke-width="1.2"/><path d="M3 8.5L1.5 11.5 5.5 9.3" fill="none" stroke="#333" stroke-width="1.2"/></svg>0</span><span class="likes">2 <svg width="15" height="13" viewBox="0 0 15 13"><path d="M7.5 12L1.6 6.2A3.3 3.3 0 017.5 2.3a3.3 3.3 0 015.9 3.9z" fill="none" stroke="#333" stroke-width="1.2"/></svg></span></div>
  </article>
  <article class="abs card" style="left:777px">
    <div class="photo" style="background:linear-gradient(135deg,#d9dadb,#5d6066 55%,#2d2f33)" role="img" aria-label="Photo of a team applauding at a meeting table"></div>
    <div class="body">
      <div class="date"><svg width="11" height="11" viewBox="0 0 11 11"><rect x="0.5" y="1.5" width="10" height="9" fill="none" stroke="#333"/><rect x="0.5" y="1.5" width="10" height="2.5" fill="#333"/></svg>Dec 23, 2021</div>
      <h3>The standard Lorem Ipsum</h3>
      <p class="excerpt">Lorem ipsum dolor sit amet, consectetur adipiscing elit, sed do eiusmod tempor incididunt</p>
    </div>
    <div class="meta"><span><svg width="16" height="10" viewBox="0 0 16 10"><ellipse cx="8" cy="5" rx="7.5" ry="4.5" fill="#333"/><circle cx="8" cy="5" r="2" fill="#fff"/></svg>0</span><span><svg width="15" height="12" viewBox="0 0 15 12"><ellipse cx="7.5" cy="5" rx="6.5" ry="4.3" fill="none" stroke="#333" stroke-width="1.2"/><path d="M3 8.5L1.5 11.5 5.5 9.3" fill="none" stroke="#333" stroke-width="1.2"/></svg>0</span><span class="likes">2 <svg width="15" height="13" viewBox="0 0 15 13"><path d="M7.5 12L1.6 6.2A3.3 3.3 0 017.5 2.3a3.3 3.3 0 015.9 3.9z" fill="none" stroke="#333" stroke-width="1.2"/></svg></span></div>
  </article>
</section>

<section class="contact">
  <h2 class="abs section-title">Get in Touch</h2>
  <div class="abs field" style="left:206px;top:177px;width:385px;height:51px">First Name</div>
  <div class="abs field" style="left:606px;top:177px;width:386px;height:51px">Last Name</div>
  <div class="abs field" style="left:206px;top:244px;width:385px;height:51px">Email</div>
  <div class="abs field" style="left:606px;top:244px;width:386px;height:51px">Phone</div>
  <div class="abs field area" style="left:206px;top:311px;width:786px;height:105px">How Can We Help?</div>
  <a class="abs btn-submit">Submit</a>
</section>

<footer class="site-footer">
  <div class="abs brand">Holvencrest Ventures</div>
  <p class="abs foot-about">Lorem ipsum dolor sit amet, consectetur adipiscing elit, sed do eiusmod tempor incididunt ut labore et dolore magna aliqua.</p>

  <div class="abs foot-col" style="left:459px">
    <h4>Contact Us</h4>
    <div class="contact-item"><svg width="16" height="16" viewBox="0 0 16 16" style="margin-top:4px"><path d="M3.5 1.5l2.5 3-1.5 2a9 9 0 004.5 4.5l2-1.5 3 2.5-1.5 2.5C7 14.5 1.5 9 1 3z" fill="#fff"/></svg><div><div class="lbl">Phone</div>+1 888 888 8888</div></div>
    <div class="contact-item"><svg width="16" height="12" viewBox="0 0 16 12" style="margin-top:8px"><rect width="16" height="12" fill="#fff"/><path d="M0 0l8 6 8-6" fill="none" stroke="#1c1c1e" stroke-width="1.4"/></svg><div><div class="lbl">Email</div>info@holvencrest.com</div></div>
  </div>

  <div class="abs foot-col" style="left:735px">
    <h4>Quick Links</h4>
    <ul class="links"><li>Home</li><li>Inspections</li><li>About Us</li><li>Expert's Corner</li><li>Contact Us</li></ul>
  </div>

  <div class="abs foot-col" style="left:939px">
    <h4>Follow On</h4>
    <div class="social"><span class="dot"></span>Linkora</div>
    <div class="social"><span class="dot"></span>Snapfold</div>
    <div class="social"><span class="dot"></span>Chirpline</div>
  </div>

  <div class="abs foot-rule"></div>
  <p class="abs copyright">Copyright ©2022, All Rights Reserved</p>
</footer>

</body>
</html>
```